Moder Business Card Design for Renewables Business

Need a business card design for my business. We collect & repurpose spent coffee ground from cafes. The cards will be made from recycled paper. Needs to fit our corporate colour scheme of white, green & brown (see logo for colour codes). Eco friendly, modern, intresting & eye catching.
This card needs to convey the message of the business and fit into its mantra of eco-friendly, sustainable etc.

Target Market(s)

Cafe Owners, Coffee Drinkers, Recycling Companies, Farmers

Industry/Entity Type

Recycling

Contact Information for Business Card

Name; Peter Halloran
Phone; 0412 386 527
e-mail; info@lumatrove.com.au
website; www.lumatrove.com.au

Font styles to use
Sans Serif
Script

Colors

Designer to choose colors to be used in the design.

Requirements
Must have
• FRONT;
• Logo, Name (Peter Halloran), phone number, e-mail address, website
• BACK;
• On the back in cursive text; 'SUSTAINABILITY IN THE DAILY GRIND'
• Small facebook & Instagram logos with text 'Lumatrove'
Should not have
• messy design

```html
<!DOCTYPE html>
<html lang="en">
<head>
<meta charset="utf-8">
<title>Lumatrove Business Card</title>
<link rel="stylesheet" href="https://fonts.googleapis.com/css2?family=Roboto+Condensed:wght@400;500&family=Mystery+Quest&display=swap">
<style>
  :root {
    --page: #e9e9ea;
    --paper: #f5f5f4;
    --ink: #3a3a3a;
    --ink-soft: #6b6b6b;
    --rule: #9a9a9a;
    --band: #454545;
    --field: #d0d0d0;
  }
  * { margin: 0; padding: 0; box-sizing: border-box; }
  html, body { width: 1200px; height: 1200px; overflow: hidden; }
  body {
    background: var(--page);
    font-family: "Roboto Condensed", Arial, sans-serif;
    color: var(--ink);
    position: relative;
  }
  .card {
    position: absolute;
    left: 150px;
    width: 900px;
    height: 514px;
    background: var(--paper);
    box-shadow: 0 6px 22px rgba(0,0,0,0.12);
    overflow: hidden;
  }
  .card--front { top: 40px; }
  .card--back { top: 646px; }

  /* Front */
  .top-band { position: absolute; left: 0; top: 0; width: 100%; height: 12px; background: var(--band); }
  .brand { position: absolute; left: 60px; top: 110px; width: 240px; text-align: center; }
  .brand__mark {
    width: 180px; height: 180px; margin: 0 auto;
    border: 8px solid var(--ink-soft); border-radius: 50%;
  }
  .brand__name {
    margin-top: 26px; font-size: 44px; font-weight: 500;
    color: var(--ink-soft); letter-spacing: 0.5px;
  }
  .divider { position: absolute; left: 355px; top: 90px; width: 1px; height: 370px; background: var(--rule); }
  .person { position: absolute; left: 405px; top: 100px; display: flex; align-items: center; gap: 18px; }
  .person__name { font-size: 40px; font-weight: 500; color: var(--ink); }
  .contacts { position: absolute; left: 405px; top: 200px; width: 420px; list-style: none; }
  .contacts li {
    display: flex; align-items: center; gap: 20px;
    height: 54px; border-bottom: 1px solid var(--rule);
    font-size: 26px; font-weight: 500; color: var(--ink);
  }
  .contacts li:first-child { border-top: 1px solid var(--rule); }
  .contacts svg { flex: none; }

  /* Back */
  .tagline {
    position: absolute; left: 90px; top: 90px; width: 720px;
    font-family: "Mystery Quest", cursive;
    font-size: 60px; line-height: 1.25; text-align: center; color: var(--ink);
    letter-spacing: 4px;
  }
  .search-rule { position: absolute; left: 110px; top: 300px; width: 690px; height: 3px; background: var(--field); }
  .search-button {
    position: absolute; left: 800px; top: 282px; width: 70px; height: 40px;
    background: var(--field); display: flex; align-items: center; justify-content: center;
  }
  .handle-field {
    position: absolute; left: 360px; top: 440px; width: 500px; height: 42px;
    border: 2px solid var(--field); padding-left: 16px;
    font-size: 22px; line-height: 38px; color: var(--ink-soft);
  }
  .social { position: absolute; left: 30px; top: 446px; display: flex; gap: 10px; }
  .social span { width: 36px; height: 36px; border-radius: 50%; background: var(--band); }
</style>
</head>
<body>

<section class="card card--front" aria-label="Business card front">
  <div class="top-band"></div>
  <div class="brand">
    <div class="brand__mark"></div>
    <div class="brand__name">LUMATROVE</div>
  </div>
  <div class="divider"></div>
  <div class="person">
    <svg width="30" height="36" viewBox="0 0 30 36" aria-hidden="true">
      <circle cx="15" cy="10" r="8" fill="#8a8a8a"/>
      <path d="M1 35 C1 24 7 20 15 20 C23 20 29 24 29 35 Z" fill="#8a8a8a"/>
    </svg>
    <span class="person__name">Peter Halloran</span>
  </div>
  <ul class="contacts">
    <li>
      <svg width="20" height="20" viewBox="0 0 20 20" aria-hidden="true"><path d="M4 2 L8 2 L9 6 L7 8 C8 11 9 12 12 13 L14 11 L18 12 L18 16 C18 17 17 18 16 18 C8 18 2 12 2 4 C2 3 3 2 4 2 Z" fill="#7a7a7a"/></svg>
      <span>0412 386 527</span>
    </li>
    <li>
      <svg width="20" height="16" viewBox="0 0 20 16" aria-hidden="true"><rect x="1" y="1" width="18" height="14" fill="#7a7a7a"/><path d="M1 1 L10 9 L19 1" stroke="#f5f5f4" stroke-width="1.5" fill="none"/></svg>
      <span>info@lumatrove.com.au</span>
    </li>
    <li>
      <svg width="20" height="20" viewBox="0 0 20 20" aria-hidden="true"><circle cx="10" cy="10" r="8.5" fill="none" stroke="#7a7a7a" stroke-width="1.8"/><ellipse cx="10" cy="10" rx="3.5" ry="8.5" fill="none" stroke="#7a7a7a" stroke-width="1.5"/><line x1="1.5" y1="10" x2="18.5" y2="10" stroke="#7a7a7a" stroke-width="1.5"/></svg>
      <span>www.lumatrove.com.au</span>
    </li>
  </ul>
</section>

<section class="card card--back" aria-label="Business card back">
  <p class="tagline">SUSTAINABILITY IN THE<br>DAILY GRIND</p>
  <div class="search-rule"></div>
  <div class="search-button">
    <svg width="22" height="22" viewBox="0 0 22 22" aria-hidden="true"><circle cx="9" cy="9" r="6.5" fill="none" stroke="#8a8a8a" stroke-width="2"/><line x1="14" y1="14" x2="20" y2="20" stroke="#8a8a8a" stroke-width="2.4"/></svg>
  </div>
  <div class="social" role="img" aria-label="Social network links">
    <span></span><span></span><span></span>
  </div>
  <div class="handle-field">Lumatrove</div>
</section>

</body>
</html>
```